ROOTS under BRANCHES : Reshaping Every Bond You Hold While Nobody Around You Has to Budge

Physical and Electronic Book Cover

Relationship is the interaction, intersection, and connection we have with every single person that we interact with. Relationship is not just the romantic relationship of your dreams. Relationships may also be the connection with our family of origin (our parents, aunts, uncles, grandparents, siblings), our friends, our coworkers, our colleagues, the people that we teach, treat, or serve and the children we create. Before we can be there with and for all those other people – before we can connect, collaborate, and create healthy, secure relationships with them – first we need to get right within our relationship to our Self. The ME needs to come before the WE.

Target Market(s)

Adults who want to improve their relationships to their friends, family, kids, coworkers and intimate partner

Industry/Entity Type

Personal Development, Relationship Coaching, Health & Wellness

Font styles to use
Serif
Decorative
Script

Colors
0054AA
0677BA
7BADD7
CADEEF
E8F1F8
EB3D1F
EC4F4E
F09395
F8D3D4
FCEDEE
E54698
E96AAD
F1A4CE
F9D9EA
FCEFF6

Requirements
Nice to have
• I'd like a strong eye catching title and graphic. I prefer blue/red jewel tones. I really enjoy creative integration of the cover design / art to the spine and back cover.
Should not have
• I would prefer not to have actual people as it gets too complicated with all the different types of relationships.

```html
<!DOCTYPE html>
<html lang="en">
<head>
<meta charset="utf-8">
<title>Roots under Branches – Book Cover</title>
<link rel="stylesheet" href="https://fonts.googleapis.com/css2?family=Playfair+Display:wght@400;500&family=Libre+Baskerville:ital,wght@0,400;1,400;1,700&family=Cormorant+Garamond:wght@500&family=Great+Vibes&display=swap">
<style>
  :root {
    --rose: #d61e5e;
    --navy: #263961;
    --cream: #f6d7bd;
    --white: #ffffff;
    --blush-top: #fcedee;
    --blush-bottom: #ef9fb8;
  }
  * { margin: 0; padding: 0; box-sizing: border-box; }
  html, body { width: 1200px; height: 864px; overflow: hidden; background: var(--navy); }
  .cover {
    position: relative;
    width: 1200px;
    height: 864px;
    overflow: hidden;
    background: linear-gradient(to bottom, var(--rose) 0, var(--rose) 373px, var(--navy) 373px, var(--navy) 100%);
  }
  .back-blurb {
    position: absolute;
    left: 68px;
    width: 440px;
    text-align: center;
    font-family: "Libre Baskerville", Georgia, serif;
    font-size: 14.6px;
    line-height: 21.4px;
    color: var(--cream);
    white-space: nowrap;
  }
  .back-blurb--top { top: 105px; }
  .back-blurb--bottom { top: 484px; }
  .author-portrait {
    position: absolute;
    left: 190px;
    top: 268px;
    width: 196px;
    height: 196px;
    border-radius: 50%;
    border: 1.5px solid var(--rose);
    background: radial-gradient(circle at 55% 45%, #c9a58e 0, #7a5a4b 35%, #3a3340 65%, #e9e7e3 100%);
  }
  .publisher-badge {
    position: absolute;
    left: 49px;
    top: 712px;
    width: 88px;
    height: 88px;
    border-radius: 50%;
    background: var(--white);
    display: flex;
    align-items: center;
    justify-content: center;
    text-align: center;
    font-family: "Libre Baskerville", Georgia, serif;
    font-size: 10.5px;
    line-height: 13px;
    color: var(--navy);
  }
  .barcode-area {
    position: absolute;
    left: 323px;
    top: 688px;
    width: 202px;
    height: 127px;
    background: #fbfbfb;
  }
  .spine-author, .spine-title {
    position: absolute;
    left: 578px;
    width: 42px;
    writing-mode: vertical-rl;
    transform: rotate(180deg);
    display: flex;
    align-items: center;
    justify-content: center;
    white-space: nowrap;
  }
  .spine-author {
    top: 112px;
    height: 252px;
    font-family: "Playfair Display", Georgia, serif;
    font-size: 22px;
    color: var(--cream);
  }
  .spine-title {
    top: 388px;
    height: 320px;
    font-family: "Playfair Display", Georgia, serif;
    font-weight: 500;
    font-size: 18px;
    letter-spacing: 0.12em;
    color: var(--white);
  }
  .spine-title .accent { color: var(--rose); margin: 0.35em 0; }
  .spine-mark {
    position: absolute;
    left: 581px;
    top: 776px;
    width: 38px;
    height: 38px;
    border-radius: 50%;
    background: var(--white);
  }
  .front-title {
    position: absolute;
    left: 621px;
    top: 0;
    width: 579px;
    height: 600px;
  }
  .tagline {
    position: absolute;
    left: 660px;
    width: 500px;
    top: 628px;
    text-align: center;
    font-family: "Libre Baskerville", Georgia, serif;
    font-style: italic;
    color: var(--cream);
  }
  .tagline__line { font-size: 14.5px; letter-spacing: 0.16em; line-height: 30px; }
  .tagline__key {
    font-weight: 700;
    font-size: 27px;
    letter-spacing: 0.24em;
    color: var(--rose);
    line-height: 30px;
  }
  .front-author {
    position: absolute;
    left: 640px;
    width: 546px;
    top: 772px;
    text-align: center;
    font-family: "Cormorant Garamond", Georgia, serif;
    font-weight: 500;
    font-size: 40px;
    line-height: 48px;
    color: var(--cream);
  }
</style>
</head>
<body>
<main class="cover">
  <!-- Back cover -->
  <p class="back-blurb back-blurb--top">Lorem ipsum dolor sit amet, consectetuer adipiscing<br>elit, sed diam nonummy nibh euismod tincidunt ut<br>laoreet dolore magna aliquam erat volutpat. Ut wisi<br>enim ad minim veniam, quis nostrud exerci tation<br>ullamcorper suscipit lobortis nisl ut aliquip ex ea<br>commodo consequat. Duis autem vel eum iriure</p>
  <div class="author-portrait" role="img" aria-label="Author portrait photograph"></div>
  <p class="back-blurb back-blurb--bottom">Lorem ipsum dolor sit amet, consectetuer adipiscing<br>elit, sed diam nonummy nibh euismod tincidunt ut<br>laoreet dolore magna aliquam erat volutpat. Ut wisi<br>enim ad minim veniam, quis nostrud exerci tation<br>ullamcorper suscipit lobortis nisl ut aliquip ex ea<br>commodo consequat. Duis autem vel eum iriure</p>
  <div class="publisher-badge">Quillfern<br>Vantor<br>Books</div>
  <div class="barcode-area"></div>

  <!-- Spine -->
  <div class="spine-author">Dr. Mara Lindqvist Hale</div>
  <div class="spine-title"><span>ROOTS</span><span class="accent">UNDER</span><span>BRANCHES</span></div>
  <div class="spine-mark"></div>

  <!-- Front cover -->
  <svg class="front-title" viewBox="621 0 579 600" aria-label="Roots under Branches">
    <defs>
      <linearGradient id="rootsFade" gradientUnits="userSpaceOnUse" x1="0" y1="220" x2="0" y2="373">
        <stop offset="0" stop-color="var(--blush-top)"/>
        <stop offset="0.5" stop-color="var(--blush-top)"/>
        <stop offset="1" stop-color="var(--blush-bottom)"/>
      </linearGradient>
    </defs>
    <text x="876" y="371" text-anchor="middle" font-family="Playfair Display, Georgia, serif" font-size="200" textLength="420" lengthAdjust="spacingAndGlyphs" fill="url(#rootsFade)">ROOTS</text>
    <text x="876" y="478" text-anchor="middle" font-family="Playfair Display, Georgia, serif" font-size="145" textLength="430" lengthAdjust="spacingAndGlyphs" fill="var(--white)">BRANCHES</text>
    <text x="790" y="492" text-anchor="middle" font-family="Great Vibes, cursive" font-size="104" fill="var(--rose)">under</text>
  </svg>

  <div class="tagline">
    <div class="tagline__line">RESHAPING EVERY</div>
    <div class="tagline__key">BOND YOU HOLD</div>
    <div class="tagline__line">WHILE NOBODY AROUND YOU HAS TO BUDGE</div>
  </div>
  <div class="front-author">Dr. Mara Lindqvist Hale</div>
</main>
</body>
</html>
```